Professional Document Wallet Design - Corporate Presentation Folder Design

Corporate Presentation Folder is known as a Document Wallet in Ireland.

This listing is for a design of a product called 'Document Wallets' - design for both inside and out. An example of the finished product is attached - 'preview document wallet.png'. This gives a clear example of what the document wallet looks like and for further details about this product you can visit this link.
http://www.presswerk-example.com/ie/group/double-gloss-lam-interlocking-presentation-folders
Attached "finish-image-1.jpg" gives an overview of the product outline as well as dimensions - also "preview document wallet"

'P10 template.indd' or 'P10 template.pdf' give the most detailed measurements of the product as these are the actual templates to be used in printing the product and therefore designs must be delivered on either of these.

Company Background

The client is a professional construction group and leads some of the largest construction jobs in the country for clients such as zentrix, novar and brelto to name a few.
The brief is to design a document wallet both sides that reflects well on their corporate clients, shows off their existing branding clearly and highlights their strengths completely.
The clients current branding can be seen at this address http://dunleavy.foxpintmedia.example/ but please be aware this website is still a work in progress.
An example of stationery styling liked by the client is found in the attached, Example of styling.pdf

Contents of the Design

As these document are a touch point for the company it is imperative that the following information is included.

1. The Company Logo
This must be clearly visible and the colouring around it enhance it's visibility. The logo should be to the fore and the design in no way should distract or detract attention from it.
2. Company Address and other contact details.
Address
Tullorren,
Carrowmeelan,
Drumlanna,
Co. Kilbarragh

T: 094 9287403
E: info@dunleavygroup.example
W: www.dunleavygroup.example

3. Some images should be included and can be found at
https://files.example.com/folderview?id=0Q_XKcTmPwRaLdNbVfGhJsYtUeZo&usp=sharing
but stock images can be used if required to ensure the most professional look and feel for the project.

Printing
UV spot printing will be used on this printing and it is a requirement of the design to incorporate this into the finished article in some way. The document wallets are double sided so the same design should run throughout and consideration given to the user opening the wallet.
Updates

Target Market(s)

Professional corporate Clients

Industry/Entity Type

Product

Requirements
Must have
• Professional
• Striking
• Branding
• Logo
• Contact details
Nice to have
• A design surrounding the business card holder o the document wallet to enhance the area where the business card is held.

```html
<!DOCTYPE html>
<html lang="en">
<head>
<meta charset="utf-8">
<title>Dunleavy Group – Document Wallet</title>
<link href="https://fonts.googleapis.com/css2?family=Roboto:wght@400;500;700&display=swap" rel="stylesheet">
<style>
  :root{
    --stage:#2a2827;
    --brand:#3a2f86;
    --sky-top:#6f9ee0;
    --sky-mid:#9cc6ee;
    --sky-pale:#dcecf8;
    --tile-border:#e8f2fb;
    --ink:#1d1a3e;
    --white:#ffffff;
  }
  html,body{margin:0;padding:0;overflow:hidden}
  body{width:1200px;height:855px;background:var(--stage);font-family:"Roboto",Arial,sans-serif;position:relative}

  /* ---------- Outside spread ---------- */
  .outside{position:absolute;left:24px;top:200px;width:520px;height:368px;display:flex}
  .back-cover,.front-cover{position:relative;width:260px;height:368px;overflow:hidden}
  .back-cover{background:linear-gradient(160deg,var(--sky-top) 0%,var(--sky-mid) 45%,var(--sky-pale) 85%)}
  .front-cover{background:linear-gradient(180deg,var(--sky-mid) 0%,var(--sky-pale) 40%,var(--sky-pale) 100%)}
  .band{position:absolute;left:0;right:0;height:17px;background:var(--brand)}
  .back-cover .band{bottom:0}
  .front-cover .band{top:0}
  .band-url{position:absolute;right:14px;top:3px;font-size:8px;letter-spacing:.6px;color:var(--white)}

  .photo-tile{position:absolute;border:3px solid var(--tile-border);box-sizing:border-box}
  .tile-stadium{left:46px;top:32px;width:57px;height:57px;background:linear-gradient(160deg,#6d7f84,#3f7d3a 60%,#8fa08f)}
  .tile-reception{left:168px;top:17px;width:69px;height:69px;background:linear-gradient(150deg,#5a3a2a,#d8d3c7 55%,#9b6b46)}
  .tile-lecture{left:102px;top:89px;width:68px;height:68px;background:linear-gradient(160deg,#c9d1d3,#5d6a70 50%,#2f3a40)}
  .tile-chapel{left:33px;top:158px;width:69px;height:69px;background:linear-gradient(170deg,#7a4d2a,#d8a664 50%,#5a3a22)}

  .wordmark{display:flex;align-items:center;gap:6px;color:var(--brand)}
  .wordmark-square{background:var(--brand);flex:none}
  .wordmark-name{font-weight:700;line-height:1;white-space:nowrap}
  .wordmark-sub{font-weight:500;line-height:1;color:var(--ink);display:flex;align-items:center;gap:4px;white-space:nowrap}
  .wordmark-sub::before,.wordmark-sub::after{content:"";height:1px;background:var(--ink);width:18px}
  .tagline{font-size:4.6px;color:var(--ink);white-space:nowrap;margin-top:3px}

  .back-logo{position:absolute;left:38px;top:256px}
  .back-logo .wordmark-square{width:20px;height:24px}
  .back-logo .wordmark-name{font-size:14px}
  .back-logo .wordmark-sub{font-size:7px;margin-top:2px}
  .contact{position:absolute;left:38px;top:290px;margin:0;font-style:normal;font-size:5.2px;line-height:6.4px;color:var(--ink)}
  .contact p{margin:0}
  .contact .gap{margin-top:5px}

  .front-logo{position:absolute;left:56px;top:45px}
  .front-logo .wordmark-square{width:30px;height:45px}
  .front-logo .wordmark-name{font-size:25px}
  .front-logo .wordmark-sub{font-size:11px;margin-top:3px}
  .front-logo .wordmark-sub::before,.front-logo .wordmark-sub::after{width:30px}

  .photo-grid{position:absolute;left:0;right:0;top:120px;bottom:0;display:grid;grid-template-columns:94px 64px 96px;grid-template-rows:44px 72px 78px 54px;gap:3px;background:var(--sky-pale)}
  .photo-grid div{width:100%;height:100%}
  .g1{background:linear-gradient(150deg,#f1f3f2,#b9c4c8)}
  .g2{background:linear-gradient(150deg,#e6e9ea,#c9d0d3)}
  .g3{background:linear-gradient(120deg,#8a5a2a,#e3c07a 50%,#7a4c22)}
  .g4{background:linear-gradient(160deg,#d8d2c4,#6a4a2e 60%,#3d2e22)}
  .g5{background:linear-gradient(160deg,#f1eee6,#b6a898 60%,#6a7a8a)}
  .g6{background:linear-gradient(150deg,#c89a52,#6a4824 55%,#d9b06c)}
  .g7{background:linear-gradient(180deg,#263a78,#4e5f7a 60%,#2c3540)}
  .g8{background:linear-gradient(180deg,#1f3a7a,#6d7d92 60%,#3a4450)}
  .g9{background:linear-gradient(180deg,#8aa0c4,#e8ecef 55%,#6d7380)}
  .g10{background:linear-gradient(180deg,#2a3550,#3b4756)}
  .g11{background:linear-gradient(180deg,#3a4a60,#2a2f38)}
  .g12{background:linear-gradient(180deg,#d9dde2,#8a6e4e)}

  /* ---------- Inside spread ---------- */
  .inside{position:absolute;left:570px;top:180px;width:614px;height:449px}
  .inside svg{display:block;width:614px;height:449px}
</style>
</head>
<body>

<section class="outside" aria-label="Document wallet outside spread">
  <div class="back-cover">
    <div class="photo-tile tile-stadium" role="img" aria-label="Aerial photo of a stadium with green pitch"></div>
    <div class="photo-tile tile-reception" role="img" aria-label="Photo of an office reception desk"></div>
    <div class="photo-tile tile-lecture" role="img" aria-label="Photo of a lecture theatre interior"></div>
    <div class="photo-tile tile-chapel" role="img" aria-label="Photo of a restored chapel interior"></div>

    <div class="back-logo">
      <div class="wordmark">
        <span class="wordmark-square"></span>
        <div>
          <div class="wordmark-name">Dunleavy</div>
          <div class="wordmark-sub">Group</div>
          <div class="tagline">Building-Joinery-Facilities-Staffing</div>
        </div>
      </div>
    </div>

    <address class="contact">
      <p>Tullorren, Carrowmeelan, Drumlanna,</p>
      <p>Co. Kilbarragh</p>
      <p class="gap">T: 094 9287403</p>
      <p>E: info@dunleavygroup.example</p>
      <p>W: www.dunleavygroup.example</p>
      <p>M: 086 5172940 / 087 3816052</p>
    </address>
    <div class="band"></div>
  </div>

  <div class="front-cover">
    <div class="band"><span class="band-url">www.dunleavygroup.example</span></div>
    <div class="front-logo">
      <div class="wordmark">
        <span class="wordmark-square"></span>
        <div>
          <div class="wordmark-name">Dunleavy</div>
          <div class="wordmark-sub">Group</div>
          <div class="tagline">Building-Joinery-Facilities-Staffing</div>
        </div>
      </div>
    </div>
    <div class="photo-grid" role="img" aria-label="Grid of project photos: interiors, timber ceiling, modern school buildings at dusk">
      <div class="g1"></div><div class="g2"></div><div class="g3"></div>
      <div class="g4"></div><div class="g5"></div><div class="g6"></div>
      <div class="g7"></div><div class="g8"></div><div class="g9"></div>
      <div class="g10"></div><div class="g11"></div><div class="g12"></div>
    </div>
  </div>
</section>

<section class="inside" aria-label="Document wallet inside spread with pocket flap">
  <svg viewBox="0 0 766 560" xmlns="http://www.w3.org/2000/svg">
    <defs>
      <linearGradient id="building-bg" x1="0" y1="0" x2="0" y2="1">
        <stop offset="0" stop-color="#dbe5ec"/>
        <stop offset="0.45" stop-color="#c9d3d8"/>
        <stop offset="0.62" stop-color="#bfd0c6"/>
        <stop offset="0.75" stop-color="#d6e2ea"/>
        <stop offset="1" stop-color="#e4eef6"/>
      </linearGradient>
      <clipPath id="collage-clip">
        <path d="M0,0 L150,0 C230,60 260,320 145,420 L0,420 Z"/>
      </clipPath>
    </defs>

    <rect x="0" y="0" width="610" height="420" fill="url(#building-bg)" role="img" aria-label="Faded photo of a modern school building behind a lawn"/>

    <g clip-path="url(#collage-clip)" role="img" aria-label="Collage of project photos: office block, wind turbines, riverside apartments, community school">
      <rect x="0" y="0" width="260" height="60" fill="#7c8f8a"/>
      <rect x="0" y="60" width="260" height="80" fill="#8a6f60"/>
      <rect x="0" y="140" width="260" height="70" fill="#3f74b8"/>
      <rect x="0" y="210" width="260" height="70" fill="#5d6f8a"/>
      <rect x="0" y="280" width="260" height="70" fill="#4a5a4e"/>
      <rect x="0" y="350" width="260" height="70" fill="#3a4f78"/>
    </g>

    <ellipse cx="0" cy="215" rx="123" ry="205" fill="#cfe1ee" opacity="0.75"/>

    <path d="M610,0 C690,0 750,170 766,420 L610,420 Z" fill="var(--brand)"/>
    <path d="M320,420 L610,420 C612,500 590,556 535,558 C445,560 360,500 320,420 Z" fill="var(--brand)"/>
  </svg>
</section>

</body>
</html>
```